'The Brookfield' @2847 Marlow Bend Road, Greenwith

Hi, We need a For Sale brochure done for a new land division. I work in Real Estate and have have listed 14 Land Allotments and would like a nice brochure done.

The land is near some green hills and the site use to be called the Kitty Haven. I thought the development could be called 'The Brookfield' 14 Premium Allotments Greenwith.

The design we would like the name of the development across the front. Some hills, or sunset, something to represent lifestyle living.

Write Up:
Premium 14 Allotments For Sale
Blocks 359m2 - 496m2

The Brookfield offers; Sunning view to the hills, convenient location to local shops, transport and schools.

Build your dream home in this premium location on the ideal sized allotment.

Be apart of something special The Brookfield Allotments will sell quickly only 14 Available

Target Market(s)

Property Buyers looking to build their dream home on a nice block of land

Industry/Entity Type

Real Estate

Colors
add136

Requirements
Must have
• Logo, Address, Some Hills, Our company details and logo,
Nice to have
• Green Hills or sunset. Professional brochure.

```html
<!DOCTYPE html>
<html lang="en">
<head>
<meta charset="utf-8">
<title>The Brookfield – 14 Premium Allotments Greenwith</title>
<link rel="stylesheet" href="https://fonts.googleapis.com/css2?family=Lato:wght@400;700;900&display=swap">
<style>
:root{
  --lime:#add136;
  --ink:#23242a;
  --paper:#ffffff;
  --backdrop:#e6e6e2;
  --sky-top:#5b8fd6;
  --sky-low:#a9cdf0;
  --hill:#5f9a2c;
  --field:#b8a47c;
}
*{margin:0;padding:0;box-sizing:border-box}
html,body{width:1200px;height:873px;overflow:hidden;background:var(--backdrop);font-family:'Lato',sans-serif;color:var(--ink)}
.page{position:absolute;top:73px;width:488px;height:691px;background:var(--paper);box-shadow:0 4px 14px rgba(0,0,0,.18)}
.page--front{left:88px}
.page--back{left:624px}
.abs{position:absolute}

/* front */
.title-band{left:18px;top:18px;width:451px;height:130px;background:var(--lime);text-align:center;overflow:hidden}
.title-band h1{font-size:38px;font-weight:700;color:var(--paper);margin-top:12px;letter-spacing:.3px;line-height:46px}
.title-band p{font-size:21px;font-weight:700;line-height:31px;margin-top:4px}
.sale-burst{left:391px;top:18px;width:78px;height:70px}
.hero{left:18px;top:149px;width:451px;height:305px;background:linear-gradient(180deg,var(--sky-top) 0%,var(--sky-low) 52%,var(--hill) 62%,#3f7a1e 100%)}
.brand-block{left:23px;top:463px;width:441px;height:130px;background:var(--lime);display:flex;align-items:center;justify-content:center;gap:12px}
.brand-mark{width:22px;height:22px;background:var(--ink)}
.brand-name{font-size:28px;font-weight:700;color:var(--ink)}
.email-tab{left:102px;top:601px;width:284px;height:28px;background:var(--ink);color:var(--paper);font-size:17px;text-align:center;line-height:29px;white-space:nowrap}
.contact-bar{left:18px;top:629px;width:451px;height:25px;background:var(--ink);color:var(--paper);font-size:17px;display:flex;justify-content:center;align-items:center;gap:36px}
.contact-bar span{display:flex;align-items:center;gap:6px}
.foot-line{left:18px;top:661px;width:451px;height:11px;background:var(--lime)}

/* back */
.offers-photo{left:18px;top:33px;width:452px;height:338px;background:linear-gradient(180deg,#9fd3ef 0%,#cfe6f2 24%,#7f8f63 30%,#5d7a3a 55%,var(--field) 80%,#9d8b66 100%)}
.offers-tag{left:18px;top:18px;width:250px;height:30px}
.offers-tag h2{position:absolute;left:7px;top:3px;font-size:18px;font-weight:700;color:var(--paper);white-space:nowrap}
.feature-line{left:0;top:0;width:488px;height:691px;pointer-events:none}
.feature-dot{width:56px;height:56px;border-radius:50%;border:4px solid var(--paper);background:linear-gradient(160deg,#c9b79a,#7d6a52)}
.feature-label{background:var(--lime);color:var(--ink);font-size:9.5px;font-weight:700;line-height:14px;padding:0 3px;border:1px solid var(--paper);white-space:nowrap}
.promo-band{left:18px;top:381px;width:452px;height:60px;background:var(--lime);font-size:18px;font-weight:700;line-height:24px;padding:6px 10px}
.map{left:42px;top:449px;width:204px;height:110px;background:linear-gradient(135deg,#e4e4df,#cfd6c8);border:3px solid var(--ink)}
.agent{left:276px;top:450px;font-size:11.5px;line-height:13px}
.agent h3{font-size:20px;font-weight:700;line-height:22px}
.agent h4{font-size:14px;font-weight:700;line-height:18px}
.agent .agent-email{margin-top:5px;font-size:12px}
.tagline-band{left:18px;top:565px;width:452px;height:60px;background:var(--lime);text-align:center;font-size:24px;font-weight:700;line-height:27px;padding-top:3px}
.page--back .contact-bar{top:633px;width:452px}
.page--back .foot-line{width:452px}
</style>
</head>
<body>

<section class="page page--front">
  <header class="abs title-band">
    <h1>The Brookfield</h1>
    <p>14 Premium Allotments Greenwith.<br>Blocks 359m2 - 496m2</p>
  </header>
  <svg class="abs sale-burst" viewBox="0 0 78 70" aria-label="For sale">
    <polygon points="78,0 78,70 70,52 60,62 58,46 44,50 50,36 28,36 44,26 4,20 40,14 30,0" fill="#23242a"/>
    <text x="50" y="24" fill="#fff" font-family="Lato, sans-serif" font-size="12" transform="rotate(-38 50 24)">for</text>
    <text x="46" y="40" fill="#fff" font-family="Lato, sans-serif" font-size="14" font-weight="700" transform="rotate(-38 46 40)">SALE</text>
  </svg>
  <div class="abs hero" role="img" aria-label="Illustration of rolling green hills under a blue sky with a tree, a small log cabin and a block size signpost"></div>
  <div class="abs brand-block">
    <span class="brand-mark"></span>
    <span class="brand-name">Glenrowan Real Estate</span>
  </div>
  <div class="abs email-tab">dale@coastlinerentals.com.au</div>
  <div class="abs contact-bar">
    <span><svg width="14" height="12" viewBox="0 0 14 12"><path d="M1 4c0-2 3-3 6-3s6 1 6 3v1h-3V3.5H4V5H1z M3 6h8l1 5H2z" fill="#fff"/></svg>0491 570 238</span>
    <span><svg width="14" height="13" viewBox="0 0 14 13"><rect x="1" y="4" width="12" height="9" fill="#fff"/><rect x="3" y="0" width="6" height="5" fill="#fff"/><rect x="4" y="6" width="6" height="1.5" fill="#23242a"/><rect x="4" y="9" width="6" height="1.5" fill="#23242a"/></svg>(08) 7100 4821</span>
  </div>
  <div class="abs foot-line"></div>
</section>

<section class="page page--back">
  <div class="abs offers-photo" role="img" aria-label="Photo of the allotment site: dry grassland with scattered trees and houses on the hills beyond"></div>
  <div class="abs offers-tag">
    <svg width="250" height="30" viewBox="0 0 250 30"><polygon points="0,0 222,0 250,30 0,30" fill="#23242a"/><polygon points="0,0 216,0 240,26 0,26" fill="#add136"/></svg>
    <h2>The Brookfield Offers :</h2>
  </div>
  <svg class="abs feature-line" viewBox="0 0 488 691"><line x1="18" y1="127" x2="448" y2="371" stroke="#fff" stroke-width="5"/></svg>
  <div class="abs feature-dot" style="left:32px;top:102px" role="img" aria-label="Photo of a modern living room"></div>
  <div class="abs feature-label" style="left:88px;top:128px">Lifestyle Living</div>
  <div class="abs feature-dot" style="left:116px;top:154px;background:linear-gradient(180deg,#9cc0de,#6f8a55)" role="img" aria-label="Photo of a view across to the hills"></div>
  <div class="abs feature-label" style="left:174px;top:180px">Sunning view to the hills</div>
  <div class="abs feature-dot" style="left:246px;top:267px;background:linear-gradient(180deg,#c9473b,#3a5a8a)" role="img" aria-label="Photo of a local convenience store"></div>
  <div class="abs feature-label" style="left:66px;top:294px;font-size:11px">Convenient location to Local Shops</div>
  <div class="abs feature-dot" style="left:314px;top:303px;background:linear-gradient(180deg,#d89a5c,#e6c531)" role="img" aria-label="Photo of yellow school buses"></div>
  <div class="abs feature-label" style="left:196px;top:337px;font-size:10.5px">Transport and Schools</div>

  <div class="abs promo-band">Be apart of something special The Brookfield Allotments will sell quickly only 14 Available</div>
  <div class="abs map" role="img" aria-label="Street map of Greenwith marking the 14 premium allotments"></div>
  <div class="abs agent">
    <h3>Dale Hartley</h3>
    <h4>Director</h4>
    <p>PO Box 392, Norwood<br>SA 5067, Suite 8, 44-50<br>Kensington Rd. Norwood<br>SA 5067</p>
    <p class="agent-email">dale@coastlinerentals.com.au</p>
  </div>
  <div class="abs tagline-band">Build your dream home in this premium<br>location on the ideal sized allotment</div>
  <div class="abs contact-bar">
    <span><svg width="14" height="12" viewBox="0 0 14 12"><path d="M1 4c0-2 3-3 6-3s6 1 6 3v1h-3V3.5H4V5H1z M3 6h8l1 5H2z" fill="#fff"/></svg>0491 570 238</span>
    <span><svg width="14" height="13" viewBox="0 0 14 13"><rect x="1" y="4" width="12" height="9" fill="#fff"/><rect x="3" y="0" width="6" height="5" fill="#fff"/><rect x="4" y="6" width="6" height="1.5" fill="#23242a"/><rect x="4" y="9" width="6" height="1.5" fill="#23242a"/></svg>(08) 7100 4821</span>
  </div>
  <div class="abs foot-line"></div>
</section>

</body>
</html>
```